Brickline Rentals podcast postcard

I've launched a podcast about apartment investing, ownership and management which is newly up on orbix and wavlino. I want to create a postcard that I can mail to my client base to get them to subscribe

```html
<!DOCTYPE html>
<html lang="en">
<head>
<meta charset="utf-8">
<title>Brickline Rentals – Podcast Postcard</title>
<link rel="stylesheet" href="https://fonts.googleapis.com/css2?family=Poppins:wght@400;600;700;800&display=swap">
<style>
:root{
  --page:#e4e4e4;
  --white:#ffffff;
  --ink:#3d3d3d;
  --purple:#3a2a8c;
  --royal:#27318f;
  --royal-light:#2f3aa6;
  --black:#1b1b1b;
  --sky:#6b9bd6;
  --sky-pale:#c9dcf0;
  --teal:#5aa9b5;
  --sand:#e8d3a6;
}
*{box-sizing:border-box;margin:0;padding:0}
html,body{width:1039px;height:1200px;overflow:hidden;background:var(--page);font-family:"Poppins",sans-serif}
.card{position:absolute;left:159px;width:720px;height:479px;background:var(--white);overflow:hidden}
.card--front{top:96px}
.card--back{top:627px}
.card svg.backdrop{position:absolute;inset:0}

/* front */
.title{position:absolute;left:35px;top:30px;font-weight:800;font-size:43px;line-height:45px;letter-spacing:-0.5px;color:var(--ink);font-family:"Poppins",sans-serif}
.title .accent{color:var(--purple);display:block}
.pillars{position:absolute;left:30px;top:157px;display:flex}
.pillar{width:121px;display:flex;flex-direction:column;align-items:center;border-right:1px solid #e2e2e2}
.pillar:last-child{border-right:none}
.pillar svg{width:58px;height:58px}
.pillar span{margin-top:10px;font-weight:600;font-size:16px;color:var(--ink);letter-spacing:0.2px}
.subscribe-band{position:absolute;left:0;top:284px;width:245px;height:41px}
.band-shape{position:absolute;inset:0}
.subscribe-label{position:absolute;left:35px;top:0;height:41px;font-weight:700;font-size:23px;color:var(--white);display:flex;align-items:center;gap:10px}
.cursor-icon{flex:none;display:block}
.pitch{position:absolute;left:35px;top:342px;font-size:16px;line-height:22px;color:var(--ink)}
.pitch b{color:var(--purple);font-weight:700}
.handle-bar{position:absolute;left:0;top:426px;width:345px;height:53px}
.channels{position:absolute;left:35px;top:0;height:53px;display:flex;align-items:center;gap:8px;font-weight:600;color:var(--white)}
.channel{display:flex;align-items:center;gap:4px;font-size:11px}
.dot{width:12px;height:12px;border-radius:50%;background:var(--purple)}
.handle{font-size:16px;margin-left:4px}

/* back */
.back-copy{position:absolute;left:35px;top:34px;color:var(--white)}
.back-copy h2{font-weight:700;font-size:32px;line-height:40px;display:flex;align-items:center;gap:12px}
.back-copy p{margin-top:6px;font-size:17px;line-height:22px;width:360px}
.back-copy p b{font-weight:700}
.back-copy .channels{position:static;height:auto;margin-top:10px}
.back-copy .dot{background:var(--white)}
.cover{position:absolute;left:35px;top:211px;width:234px;height:232px;border:4px solid var(--white);background:linear-gradient(160deg,var(--teal) 0%,#6fb8c0 40%,var(--sand) 60%,var(--teal) 100%);box-shadow:0 6px 12px rgba(0,0,0,.25)}
.stamp{position:absolute;left:593px;top:36px;width:92px;height:92px;border:1px solid #dcdcdc}
</style>
</head>
<body>

<section class="card card--front">
  <svg class="backdrop" width="720" height="479" viewBox="0 0 720 479">
    <defs>
      <linearGradient id="sky" x1="0" y1="0" x2="0.3" y2="1">
        <stop offset="0" stop-color="#6b9bd6"/>
        <stop offset="0.45" stop-color="#c9dcf0"/>
        <stop offset="1" stop-color="#dfe6ee"/>
      </linearGradient>
    </defs>
    <polygon points="325,0 720,0 720,472 342,472 351,290 426,217" fill="url(#sky)" role="img" aria-label="Photo of a modern white apartment building with balconies against a blue sky"/>
    <rect x="340" y="472" width="380" height="7" fill="var(--purple)"/>
  </svg>

  <h1 class="title">BRICKLINE<span class="accent">RENTALS</span></h1>

  <div class="pillars">
    <div class="pillar">
      <svg viewBox="0 0 58 58"><circle cx="29" cy="29" r="26" fill="none" stroke="var(--ink)" stroke-width="4"/><path d="M29 55 A26 26 0 0 1 29 3" fill="none" stroke="var(--purple)" stroke-width="4"/><circle cx="29" cy="25" r="8" fill="none" stroke="var(--ink)" stroke-width="1.4"/><text x="29" y="29" text-anchor="middle" font-size="11" font-family="Poppins,sans-serif" fill="var(--ink)">$</text><path d="M15 38 h6 l8 3 h10 l5 -4" fill="none" stroke="var(--ink)" stroke-width="1.4"/></svg>
      <span>INVESTING</span>
    </div>
    <div class="pillar">
      <svg viewBox="0 0 58 58"><circle cx="29" cy="29" r="26" fill="none" stroke="var(--ink)" stroke-width="4"/><path d="M29 55 A26 26 0 0 1 29 3" fill="none" stroke="var(--purple)" stroke-width="4"/><path d="M17 29 L29 18 L41 29 M20 27 V41 H38 V27" fill="none" stroke="var(--ink)" stroke-width="1.4"/><rect x="26" y="32" width="6" height="9" fill="none" stroke="var(--ink)" stroke-width="1.4"/></svg>
      <span>OWNING</span>
    </div>
    <div class="pillar">
      <svg viewBox="0 0 58 58"><circle cx="29" cy="29" r="26" fill="none" stroke="var(--ink)" stroke-width="4"/><path d="M29 55 A26 26 0 0 1 29 3" fill="none" stroke="var(--purple)" stroke-width="4"/><circle cx="29" cy="27" r="7" fill="none" stroke="var(--ink)" stroke-width="1.4"/><circle cx="29" cy="27" r="11" fill="none" stroke="var(--ink)" stroke-width="1.4" stroke-dasharray="3 3"/><path d="M25 40 h8 M26 43 h6" stroke="var(--ink)" stroke-width="1.4"/></svg>
      <span>MANAGING</span>
    </div>
  </div>

  <div class="subscribe-band">
    <svg class="band-shape" width="245" height="41" viewBox="0 0 245 41"><polygon points="0,0 225,0 245,41 0,41" fill="var(--purple)"/></svg>
    <div class="subscribe-label">SUBSCRIBE
      <svg class="cursor-icon" width="24" height="24" viewBox="0 0 24 24"><path d="M9 7 L20 16 L15 16 L18 22 L16 23 L13 17 L9 20 Z" fill="var(--white)"/><path d="M6 2 v4 M1 7 h4 M2 3 l3 3 M10 3 l-2 3" stroke="var(--white)" stroke-width="1.5"/></svg>
    </div>
  </div>

  <p class="pitch">I've launched a <b>podcast</b> which<br>is newly up on <b>orbix</b> and <b>wavlino</b>.</p>

  <div class="handle-bar">
    <svg class="band-shape" width="345" height="53" viewBox="0 0 345 53"><polygon points="0,0 313,0 338,53 0,53" fill="var(--black)"/></svg>
    <div class="channels">
      <span class="channel"><i class="dot"></i>wavlino</span>
      <span class="channel"><i class="dot"></i>orbix</span>
      <span class="handle">@bricklinerentals</span>
    </div>
  </div>
</section>

<section class="card card--back">
  <svg class="backdrop" width="720" height="479" viewBox="0 0 720 479">
    <polygon points="0,0 499,0 271,479 0,479" fill="var(--royal)"/>
    <polygon points="440,0 499,0 271,479 240,479" fill="var(--royal-light)" opacity="0.6"/>
  </svg>

  <div class="back-copy">
    <h2>SUBSCRIBE
      <svg class="cursor-icon" width="30" height="30" viewBox="0 0 24 24"><path d="M9 7 L20 16 L15 16 L18 22 L16 23 L13 17 L9 20 Z" fill="var(--white)"/><path d="M6 2 v4 M1 7 h4 M2 3 l3 3 M10 3 l-2 3" stroke="var(--white)" stroke-width="1.5"/></svg>
    </h2>
    <p>My <b>podcast</b> about apartment investing, ownership and management which is newly up on <b>orbix</b> and <b>wavlino</b>.</p>
    <div class="channels">
      <span class="channel"><i class="dot"></i>wavlino</span>
      <span class="channel"><i class="dot"></i>orbix</span>
      <span class="handle">@bricklinerentals</span>
    </div>
  </div>

  <div class="cover" role="img" aria-label="Podcast cover art: apartment building against a teal sky with the show title"></div>
  <div class="stamp"></div>
</section>

</body>
</html>
```